Music Poster (that is birthday gift.)

We want a rock music poster in the spirit of the old time Copperfield Lantern psychedelic posters that says, "Brackley Summer Music Festival" "July 30, 2016." Red Hook, NY. Dustin Yates is the artist. This is the 4th Annual Event. It is also Neil Brackley's 50th birthday.
Happy to answer any questions on email or live. Call Gordon at 555.381.4926

Target Market(s)

Personal gift!

Industry/Entity Type

Festival

Requirements
Must have
• Fabulous Design....

```html
<!DOCTYPE html>
<html lang="en">
<head>
<meta charset="utf-8">
<title>Brackley Summer Music Festival</title>
<link href="https://fonts.googleapis.com/css2?family=Bagel+Fat+One&display=swap" rel="stylesheet">
<style>
  :root {
    --stage: #111111;
    --poster-edge: #351a63;
    --poster-field: #6a2b9c;
    --field-glow: #7833ad;
    --field-deep: #45197a;
    --frame-line: #ffffff;
    --ink-cyan: #8fd6e2;
    --ink-edge: #3f1670;
    --portrait-light: #d9eff3;
    --portrait-mid: #9db3b8;
    --portrait-dark: #22343a;
  }
  * { margin: 0; padding: 0; box-sizing: border-box; }
  html, body { width: 1200px; height: 1200px; overflow: hidden; background: var(--stage); }
  .poster {
    position: absolute; left: 206px; top: 42px; width: 790px; height: 1116px;
    background: var(--poster-edge);
  }
  .poster-frame {
    position: absolute; left: 20px; top: 20px; right: 20px; bottom: 24px;
    border: 4px solid var(--frame-line); background: var(--poster-field); overflow: hidden;
  }
  .poster-art { position: absolute; inset: 0; width: 100%; height: 100%; display: block; }
  .lettering text {
    font-family: 'Bagel Fat One', sans-serif; font-size: 100px;
    fill: var(--ink-cyan); stroke: var(--ink-edge); stroke-width: 2.5px;
    paint-order: stroke fill; text-transform: uppercase;
  }
  .field-deep { fill: var(--field-deep); }
  .field-glow { fill: var(--field-glow); }
</style>
</head>
<body>
  <div class="poster">
    <div class="poster-frame">
      <svg class="poster-art" viewBox="0 0 742 1064" preserveAspectRatio="none">
        <defs>
          <linearGradient id="portrait-tone" x1="0" y1="0" x2="0.35" y2="1">
            <stop offset="0" stop-color="var(--portrait-dark)"/>
            <stop offset="0.28" stop-color="var(--portrait-dark)"/>
            <stop offset="0.42" stop-color="var(--portrait-light)"/>
            <stop offset="0.75" stop-color="var(--portrait-mid)"/>
            <stop offset="1" stop-color="var(--portrait-light)"/>
          </linearGradient>
        </defs>

        <g class="field-shapes" aria-hidden="true">
          <path class="field-deep" d="M600 0 C700 20 742 80 742 160 L742 0 Z"/>
          <path class="field-glow" d="M300 200 C420 150 560 170 620 250 C700 350 690 470 600 520 C480 580 340 520 300 420 C270 340 250 250 300 200 Z"/>
          <path class="field-deep" d="M742 880 C728 960 704 1020 670 1064 L742 1064 Z"/>
          <path class="field-deep" d="M0 540 C10 700 6 860 0 960 Z"/>
        </g>

        <g class="lettering headline">
          <text transform="translate(10 98) scale(1 1.22)" textLength="560" lengthAdjust="spacingAndGlyphs">Brackley</text>
          <text transform="translate(10 198) scale(1 1.28)" textLength="552" lengthAdjust="spacingAndGlyphs">Summer</text>
          <text transform="translate(10 446) scale(1 3)" textLength="280" lengthAdjust="spacingAndGlyphs">Music</text>
          <text transform="translate(314 382) scale(1 1.67)" textLength="62" lengthAdjust="spacingAndGlyphs">F</text>
          <text transform="translate(378 406) scale(1 1.89)" textLength="52" lengthAdjust="spacingAndGlyphs">E</text>
          <text transform="translate(434 422) scale(1 2.33)" textLength="52" lengthAdjust="spacingAndGlyphs">S</text>
          <text transform="translate(490 430) scale(1 2.89)" textLength="48" lengthAdjust="spacingAndGlyphs">T</text>
          <text transform="translate(546 446) scale(1 3.78)" textLength="32" lengthAdjust="spacingAndGlyphs">I</text>
          <text transform="translate(586 462) scale(1 4.67)" textLength="56" lengthAdjust="spacingAndGlyphs">V</text>
          <text transform="translate(648 478) scale(1 5.33)" textLength="48" lengthAdjust="spacingAndGlyphs">A</text>
          <text transform="translate(700 486) scale(1 6.33)" textLength="32" lengthAdjust="spacingAndGlyphs">L</text>
        </g>

        <path class="portrait" role="img" aria-label="Illustrated portrait of the guest artist in pale cyan, grey and dark teal tones"
              fill="url(#portrait-tone)"
              d="M0 1064 L0 960 C50 944 110 930 134 900 L130 580 C130 500 200 450 290 450 C380 450 420 500 420 580 L418 700 C410 760 396 790 396 840 L396 920 C420 960 470 1010 500 1064 Z"/>

        <g class="lettering billing">
          <text transform="translate(422 580) scale(1 1.11)" textLength="110" lengthAdjust="spacingAndGlyphs">With</text>
          <text transform="translate(538 540) scale(1 0.64)" textLength="194" lengthAdjust="spacingAndGlyphs">Special</text>
          <text transform="translate(540 590) scale(1 0.61)" textLength="190" lengthAdjust="spacingAndGlyphs">Guest</text>
          <text transform="translate(440 684) scale(1 1.17)" textLength="292" lengthAdjust="spacingAndGlyphs">Dustin</text>
          <text transform="translate(422 800) scale(1 1.39)" textLength="308" lengthAdjust="spacingAndGlyphs">Yates</text>
        </g>

        <g class="lettering place">
          <text transform="translate(10 598) rotate(90) scale(1 0.72)" textLength="160" lengthAdjust="spacingAndGlyphs">Red</text>
          <text transform="translate(66 670) rotate(90) scale(1 0.78)" textLength="152" lengthAdjust="spacingAndGlyphs">Hook</text>
          <text transform="translate(10 918) scale(1 1.11)" textLength="118" lengthAdjust="spacingAndGlyphs">NY</text>
        </g>

        <g class="lettering date">
          <text transform="translate(402 830) scale(1 0.36)" textLength="176" lengthAdjust="spacingAndGlyphs">July 30th</text>
          <text transform="translate(402 910) scale(1 0.97)" textLength="172" lengthAdjust="spacingAndGlyphs">2016</text>
        </g>

        <g class="lettering occasion">
          <text transform="translate(598 888) scale(1 1.08)" textLength="134" lengthAdjust="spacingAndGlyphs">Neil</text>
          <text transform="translate(586 952) scale(1 0.61)" textLength="146" lengthAdjust="spacingAndGlyphs">Brackley's</text>
          <text transform="translate(586 998) scale(1 0.53)" textLength="80" lengthAdjust="spacingAndGlyphs">50th</text>
          <text transform="translate(586 1046) scale(1 0.56)" textLength="146" lengthAdjust="spacingAndGlyphs">Birthday</text>
        </g>
      </svg>
    </div>
  </div>
</body>
</html>
```